Poster

I need a poster for my business, www.coastaltablejourneysbay.example which some information about the most important activities (Sangria Tasting, Iberian Ham, Charcuteries & Sherry Wine Tasting, Sailboat Experiences and Picnic Experiences). A3 Format. Social media included (@coastaltablejourneyctj), contact information included.

```html
<!DOCTYPE html>
<html lang="en">
<head>
<meta charset="utf-8">
<title>Coastal Table Journeys Bay – Poster</title>
<link rel="stylesheet" href="https://fonts.googleapis.com/css2?family=Bebas+Neue&family=Kaushan+Script&family=Montserrat:ital,wght@0,500;1,500&display=swap">
<style>
  :root {
    --page-bg: #d9d9d9;
    --sea-deep: #0f2557;
    --sea-mid: #1a3c86;
    --sea-light: #2b58a8;
    --panel-shade: rgba(12, 30, 72, 0.55);
    --white: #ffffff;
    --ink: #2e2e2e;
    --accent: #f0a21e;
    --chat-green: #3cc44a;
    --social-blue: #4a67ad;
    --social-pink: #e2457a;
  }
  * { box-sizing: border-box; margin: 0; padding: 0; }
  html, body { width: 1200px; height: 1200px; overflow: hidden; }
  body { background: var(--page-bg); position: relative; font-family: "Bebas Neue", sans-serif; }

  .poster {
    position: absolute; left: 204px; top: 40px;
    width: 792px; height: 1120px; overflow: hidden;
    color: var(--white);
  }
  .poster-photo {
    position: absolute; inset: 0;
    background:
      radial-gradient(ellipse 60% 18% at 45% 75%, rgba(190, 225, 245, 0.45), transparent 70%),
      linear-gradient(160deg, var(--sea-light) 0%, var(--sea-mid) 45%, var(--sea-deep) 100%);
  }
  .headline-panel {
    position: absolute; left: 55px; top: 0; width: 274px; height: 557px;
    background: var(--panel-shade);
  }

  .brand-box {
    position: absolute; left: 28px; top: 37px; width: 326px; height: 174px;
    background: var(--white);
    display: flex; align-items: center; gap: 18px; padding: 0 28px;
  }
  .brand-mark { width: 26px; height: 26px; background: var(--accent); flex: none; }
  .brand-name {
    color: var(--ink); font-size: 42px; line-height: 0.95; letter-spacing: 0.5px;
  }

  .headline { position: absolute; left: 74px; top: 252px; }
  .headline-line { display: block; font-size: 128px; line-height: 0.79; letter-spacing: -1px; }
  .headline-script {
    position: absolute; left: 28px; top: 178px;
    font-family: "Kaushan Script", cursive; color: var(--accent);
    font-size: 92px; line-height: 1; transform: rotate(-6deg);
  }

  .activity {
    position: absolute; border-left: 2px solid var(--white);
    padding-left: 10px; font-size: 50px; line-height: 0.84;
  }
  .activity span { display: block; }

  .contact { position: absolute; left: 38px; top: 992px; }
  .chat-icon {
    position: absolute; left: 0; top: 0; width: 64px; height: 64px;
    border-radius: 50%; background: var(--chat-green);
  }
  .phone { position: absolute; left: 76px; top: -2px; font-size: 80px; line-height: 1; white-space: nowrap; }
  .website {
    position: absolute; left: 8px; top: 72px; font-size: 35px; line-height: 1;
    color: var(--accent); text-transform: uppercase; white-space: nowrap; letter-spacing: -0.5px;
  }
  .divider { position: absolute; left: 540px; top: 1000px; width: 1px; height: 92px; background: var(--white); }
  .social-dot { position: absolute; top: 1003px; width: 52px; height: 52px; border-radius: 50%; }
  .social-dot.one { left: 609px; background: var(--social-blue); }
  .social-dot.two { left: 669px; background: var(--social-pink); }
  .handle {
    position: absolute; left: 556px; top: 1074px;
    font-family: "Montserrat", sans-serif; font-style: italic; font-weight: 500; font-size: 14.5px;
  }
</style>
</head>
<body>
  <main class="poster">
    <div class="poster-photo" role="img" aria-label="Aerial photo of deep blue sea with a speedboat leaving a white wake"></div>
    <div class="headline-panel"></div>

    <div class="brand-box">
      <span class="brand-mark"></span>
      <span class="brand-name">Coastal Table<br>Journeys Bay</span>
    </div>

    <h1 class="headline">
      <span class="headline-line">Enjoy</span>
      <span class="headline-line">Your</span>
      <span class="headline-script">Day</span>
    </h1>

    <div class="activity" style="left:356px; top:254px;"><span>Sangria</span><span>Tasting</span></div>
    <div class="activity" style="left:534px; top:254px;"><span>Sailboat</span><span>Experiences</span></div>
    <div class="activity" style="left:356px; top:359px;"><span>Iberian</span><span>Ham</span></div>
    <div class="activity" style="left:534px; top:359px;"><span>Picnic</span><span>Experiences</span></div>
    <div class="activity" style="left:356px; top:462px;"><span>Charcuteries &amp;</span><span>Sherry Wine Tasting</span></div>

    <div class="contact">
      <span class="chat-icon"></span>
      <span class="phone">+34 611 22 33 44</span>
      <span class="website">www.coastaltablejourneysbay.example</span>
    </div>
    <span class="divider"></span>
    <span class="social-dot one"></span>
    <span class="social-dot two"></span>
    <span class="handle">@coastaltablejourneyctj</span>
  </main>
</body>
</html>
```